Rollvane Supply .com

This website is simple!!!
Landing page background image should capture the customers attention!!! We will provide a image as a example of what we like. The purpose for this website is to provide customers with a clean easy way to request a quote for industrial casters and wheels by OEM’s as well as maintenance departments worldwide. Please see if you can follow our thought process below.
Customer comes to website, they are invited to Request a Quote by providing us with Manufacturer Name, Manufacturers Part # and quantity needed.
If this is not known the customer will complete will WP conversation format form answering about 10 questions
Or
Look up the part number in one of the 8 to 12 catalogs located in the Pagewhirl Deck format on our catalog page, or equal plug in .
When the client request a quote a account page will pop up request The following:
Clients first and last name
Email address
And optional questions
Company name and best contact number.
Once this is complete customer will hit SUBMIT.
The customers request will be in system. A email will be sent to Customer service notifying us the Quote Request has been made.
We will then build a quote for the customer with a good, better and best options. Customers Request a Quote submission may have more than one caster or wheel requested at a time, so website must allow this.
When the customer comes back into website there email address will come up as the account name and request a password be made for them. This will allow them to store quotes in their account for future needs. If quote is older than 30 day the system will trigger a button at the bottom of the quote for resubmit Request for updated quote.
Once customer reviews quote the quote can be Converted to order within the website.
Once Converted the system will send us a email and order will be processed.
We will need a Chat program that will text to CS the questions.
You will need to have high quality graphic design skills on your team.
We have found 2 plugins that would work nicely with our new website Pagewhirl decks to showcase our catalogs for customers to research and QuillKit conversation forms to complete request for quote form.
Just Ideas:
Very very ghosted caster blueprint in white background but very very ghosted or the icon just idea
We have never had a font used we like
Grayscale every except for rubber on wheels and logo icon
Website should have hamburger menu on left
Website should hav responsive deign
Account head on right side
Has anyone read the brief from top to bottom and the updates, I’m seeing a lot of duplicates of the website I posted in images I want a clean website With lite backgrand with the poly being definite colors on each wheel I added a green yellow and red image has anyone looked at that Just a question?
Went on vacation/holiday

```html
<!DOCTYPE html>
<html lang="en">
<head>
<meta charset="utf-8">
<title>Rollvane Supply .com — Quote Flow</title>
<link href="https://fonts.googleapis.com/css2?family=Oswald:wght@300;400;500&family=Montserrat:wght@400;600;700&display=swap" rel="stylesheet">
<style>
  :root {
    --brand-blue: #2a44a1;
    --brand-blue-deep: #1f358a;
    --ink: #353535;
    --ink-dark: #3c3c3c;
    --paper: #f2f2f2;
    --paper-shade: #e5e5e5;
    --field: #ffffff;
    --field-line: #d9d9d9;
    --placeholder: #707070;
    --overlay: #2f2e33;
    --board: #ffffff;
  }
  html, body { margin: 0; padding: 0; overflow: hidden; background: var(--board); }
  .board { width: 1189px; height: 1200px; overflow: hidden; }
  .board svg { display: block; }

  .screen-bg { fill: url(#paper-tone); }
  .band { fill: var(--brand-blue); }
  .overlay { fill: var(--overlay); }

  .brand-name { font-family: "Montserrat", sans-serif; font-weight: 700; fill: var(--brand-blue); }
  .headline { font-family: "Oswald", sans-serif; font-weight: 400; fill: var(--ink); letter-spacing: 0.3px; }
  .screen-title { font-family: "Oswald", sans-serif; font-weight: 400; fill: var(--ink); font-size: 16px; letter-spacing: 0.6px; text-anchor: middle; }
  .modal-title { font-family: "Oswald", sans-serif; font-weight: 400; fill: var(--brand-blue); font-size: 12px; letter-spacing: 0.4px; text-anchor: middle; }
  .tagline { font-family: "Oswald", sans-serif; font-weight: 400; fill: var(--brand-blue); font-size: 9px; }
  .step-label { font-family: "Oswald", sans-serif; font-weight: 400; fill: var(--brand-blue); font-size: 10px; letter-spacing: 0.3px; }
  .step-num { font-family: "Oswald", sans-serif; font-weight: 400; fill: var(--brand-blue); font-size: 8px; text-anchor: middle; }
  .question { font-family: "Oswald", sans-serif; font-weight: 500; fill: var(--brand-blue); font-size: 6.2px; letter-spacing: 0.2px; }
  .field { fill: var(--field); stroke: var(--field-line); stroke-width: 0.8; }
  .placeholder { font-family: "Montserrat", sans-serif; font-size: 6px; fill: var(--placeholder); }
  .btn-blue { fill: var(--brand-blue); }
  .btn-dark { fill: var(--ink-dark); }
  .btn-label { font-family: "Oswald", sans-serif; font-weight: 400; fill: #fff; font-size: 5.6px; letter-spacing: 0.3px; text-anchor: middle; }
  .or-line { stroke: #9a9a9a; stroke-width: 0.8; }
  .or-badge { fill: var(--paper); stroke: #9a9a9a; stroke-width: 0.8; }
  .or-text { font-family: "Oswald", sans-serif; fill: var(--brand-blue); font-size: 9px; text-anchor: middle; }
  .footer-text { font-family: "Montserrat", sans-serif; font-size: 5.6px; fill: #555; text-anchor: middle; }
  .footer-text .em { fill: var(--brand-blue); font-weight: 600; }
  .catalogue-label { font-family: "Oswald", sans-serif; font-weight: 400; fill: var(--ink); font-size: 9.5px; letter-spacing: 0.4px; text-anchor: middle; }
  .flow-arrow { stroke: var(--brand-blue); stroke-width: 1.1; fill: none; }
  .chevron { stroke: #555; stroke-width: 0.9; fill: none; }
  .dimmed { opacity: 0.18; }
</style>
</head>
<body>
<div class="board">
<svg width="1189" height="1200" viewBox="0 0 1920 1920" preserveAspectRatio="none" xmlns="http://www.w3.org/2000/svg">
  <defs>
    <linearGradient id="paper-tone" x1="0" y1="0" x2="1" y2="1">
      <stop offset="0" stop-color="#f5f5f5"/>
      <stop offset="0.5" stop-color="#ececec"/>
      <stop offset="1" stop-color="#f3f3f3"/>
    </linearGradient>
    <radialGradient id="caster-tone" cx="0.45" cy="0.4" r="0.6">
      <stop offset="0" stop-color="#e8e8e8"/>
      <stop offset="0.6" stop-color="#a9a9a9"/>
      <stop offset="1" stop-color="#5d5d5d"/>
    </radialGradient>
    <radialGradient id="caster-tone-warm" cx="0.45" cy="0.45" r="0.6">
      <stop offset="0" stop-color="#ead9cf"/>
      <stop offset="0.6" stop-color="#b89a8b"/>
      <stop offset="1" stop-color="#5a5656"/>
    </radialGradient>
    <marker id="arrow-head" viewBox="0 0 10 10" refX="9" refY="5" markerWidth="7" markerHeight="7" orient="auto-start-reverse">
      <path d="M0,0 L10,5 L0,10 Z" fill="var(--brand-blue)"/>
    </marker>

    <symbol id="brand-crest" viewBox="-80 0 160 85">
      <path d="M-80,0 A80,80 0 0 0 80,0 Z" fill="#e6e6e6"/>
      <path d="M-63,49 A80,80 0 0 0 63,49" fill="none" stroke="var(--brand-blue)" stroke-width="3"/>
      <circle cx="-44" cy="30" r="4" fill="var(--brand-blue)"/>
      <text class="brand-name" x="4" y="33" font-size="8.5" text-anchor="middle">Rollvane Supply .com</text>
    </symbol>

    <symbol id="footer-wave" viewBox="0 0 736 50">
      <path d="M80,50 Q368,-22 640,50 Z" fill="var(--paper-shade)"/>
      <path d="M80,50 Q368,-22 640,50" fill="none" stroke="var(--brand-blue)" stroke-width="3"/>
    </symbol>

    <symbol id="pdf-pin" viewBox="-30 -30 60 66">
      <circle cx="0" cy="0" r="26" fill="#fff" stroke="var(--brand-blue)" stroke-width="2.5"/>
      <path d="M-6,25 L0,33 L6,25 Z" fill="var(--brand-blue)"/>
      <path d="M-12,-6 V12 H8" fill="none" stroke="var(--brand-blue)" stroke-width="2"/>
      <rect x="-8" y="-13" width="22" height="21" rx="2" fill="var(--brand-blue)"/>
      <text x="3" y="0" font-family="Montserrat, sans-serif" font-weight="700" font-size="8" fill="#fff" text-anchor="middle">PDF</text>
    </symbol>
  </defs>

  <!-- ========== Landing ========== -->
  <g class="screen landing">
    <rect class="screen-bg" x="77" y="420" width="735" height="413"/>
    <polygon class="band" points="578,420 812,420 812,456 665,833 417,833"/>
    <g role="img" aria-label="Photo of a swivel caster with brake on a steel top plate">
      <ellipse cx="658" cy="535" rx="72" ry="62" fill="url(#caster-tone)"/>
    </g>
    <g role="img" aria-label="Photo of a heavy-duty swivel caster with a large polyurethane wheel">
      <ellipse cx="578" cy="722" rx="72" ry="76" fill="url(#caster-tone-warm)"/>
    </g>

    <circle cx="211" cy="540" r="9" fill="var(--brand-blue)"/>
    <text class="brand-name" x="227" y="545" font-size="13">Rollvane Supply .com</text>

    <text class="headline" x="199" y="612" font-size="16.5">#1 SOLUTIONS FOR ALL YOUR</text>
    <text class="headline" x="199" y="634" font-size="16.5">APPLICATIONS.</text>
    <text class="tagline" x="199" y="657">EASY AS 1-2-3</text>

    <g class="steps">
      <circle cx="210" cy="679" r="9" fill="none" stroke="var(--brand-blue)" stroke-width="2"/>
      <text class="step-num" x="210" y="682">1</text>
      <text class="step-label" x="231" y="684">REQUEST A QUOTE</text>
      <circle cx="210" cy="710" r="9" fill="none" stroke="var(--brand-blue)" stroke-width="2"/>
      <text class="step-num" x="210" y="713">2</text>
      <text class="step-label" x="231" y="715">RECEIVE A QUOTE</text>
      <circle cx="210" cy="740" r="9" fill="none" stroke="var(--brand-blue)" stroke-width="2"/>
      <text class="step-num" x="210" y="743">3</text>
      <text class="step-label" x="231" y="745">CONVERT A QUOTE TO ORDER.</text>
    </g>

    <rect class="btn-blue" x="199" y="769" width="69" height="20" rx="10"/>
    <text class="btn-label" x="233.5" y="781">REQUEST A QUOTE</text>
    <rect class="btn-dark" x="276" y="769" width="69" height="20" rx="10"/>
    <text class="btn-label" x="310.5" y="781">OUR CATALOGUE</text>
  </g>

  <!-- ========== Details modal ========== -->
  <g class="screen details-modal">
    <rect class="overlay" x="1099" y="80" width="736" height="414"/>
    <g class="dimmed">
      <polygon fill="#5a6fc0" points="1099,80 1221,80 1099,420"/>
      <polygon fill="#5a6fc0" points="1835,180 1835,494 1716,494"/>
      <use href="#brand-crest" x="1387" y="80" width="160" height="85"/>
      <ellipse cx="1165" cy="170" rx="48" ry="42" fill="url(#caster-tone)"/>
      <ellipse cx="1768" cy="410" rx="48" ry="52" fill="url(#caster-tone-warm)"/>
      <rect class="btn-blue" x="1337" y="398" width="110" height="18" rx="9"/>
      <rect class="btn-dark" x="1456" y="398" width="140" height="18" rx="9"/>
      <use href="#footer-wave" x="1099" y="449" width="736" height="45"/>
    </g>
    <g role="img" aria-label="Dimmed caster photos behind the form">
      <rect x="1099" y="80" width="0" height="0" fill="none"/>
    </g>

    <rect x="1333" y="180" width="268" height="214" fill="#fff"/>
    <circle cx="1599" cy="180" r="9" fill="var(--brand-blue)" stroke="#fff" stroke-width="1.5"/>
    <path d="M1596,177 L1602,183 M1602,177 L1596,183" stroke="#fff" stroke-width="1.2"/>
    <text class="modal-title" x="1467" y="208">FILL YOUR DETAILS</text>

    <rect class="field" x="1348" y="230" width="115" height="18"/>
    <text class="placeholder" x="1355" y="241">First Name</text>
    <rect class="field" x="1471" y="230" width="115" height="18"/>
    <text class="placeholder" x="1478" y="241">Last Name</text>
    <rect class="field" x="1348" y="257" width="238" height="18"/>
    <text class="placeholder" x="1355" y="268">Email</text>
    <rect class="field" x="1348" y="284" width="115" height="18"/>
    <text class="placeholder" x="1355" y="295">Company Name</text>
    <rect class="field" x="1471" y="284" width="115" height="18"/>
    <text class="placeholder" x="1478" y="295">Phone</text>
    <rect class="field" x="1348" y="310" width="238" height="38"/>
    <text class="placeholder" x="1355" y="322">Message ...</text>

    <rect class="btn-blue" x="1436" y="356" width="62" height="19" rx="9.5"/>
    <text class="btn-label" x="1467" y="367.5">SUBMIT</text>
  </g>

  <!-- ========== Questions ========== -->
  <g class="screen questions">
    <rect class="screen-bg" x="1099" y="551" width="736" height="791"/>
    <polygon class="band" points="1099,551 1221,551 1099,868"/>
    <polygon class="band" points="1835,1025 1835,1342 1716,1342"/>
    <g role="img" aria-label="Photo of a swivel caster with brake">
      <ellipse cx="1168" cy="645" rx="50" ry="46" fill="url(#caster-tone)"/>
    </g>
    <g role="img" aria-label="Photo of a heavy-duty caster with polyurethane wheel">
      <ellipse cx="1766" cy="1260" rx="50" ry="55" fill="url(#caster-tone-warm)"/>
    </g>
    <use href="#brand-crest" x="1387" y="551" width="160" height="85"/>
    <text class="screen-title" x="1467" y="686">ANSWER FOR THESE QUESTIONS</text>

    <g class="question-list">
      <text class="question" x="1279" y="713">LOREM IPSUM IS SIMPLY DUMMY TEXT OF THE PRINTING?</text>
      <rect class="field" x="1279" y="721" width="375" height="19"/>
      <text class="question" x="1279" y="759">THERE ARE MANY VARIATIONS OF PASSAGES?</text>
      <rect class="field" x="1279" y="767" width="375" height="19"/>
      <text class="question" x="1279" y="805">CONTRARY TO POPULAR BELIEF, LOREM IPSUM?</text>
      <rect class="field" x="1279" y="813" width="375" height="19"/>
      <path class="chevron" d="M1642,821 L1644.5,823.5 L1647,821"/>
      <text class="question" x="1279" y="851">LOREM IPSUM IS SIMPLY DUMMY TEXT OF THE PRINTING?</text>
      <rect class="field" x="1279" y="859" width="375" height="19"/>
      <text class="question" x="1279" y="897">CONTRARY TO POPULAR BELIEF, LOREM IPSUM?</text>
      <rect class="field" x="1279" y="905" width="375" height="19"/>
      <text class="question" x="1279" y="943">THERE ARE MANY VARIATIONS OF PASSAGES?</text>
      <rect class="field" x="1279" y="951" width="375" height="19"/>
      <path class="chevron" d="M1642,959 L1644.5,961.5 L1647,959"/>
      <text class="question" x="1279" y="989">SED UT PERSPICIATIS UNDE OMNIS ISTE NATUS?</text>
      <rect class="field" x="1279" y="997" width="375" height="19"/>
      <text class="question" x="1279" y="1035">BUT I MUST EXPLAIN TO YOU HOW ALL THIS MISTAKEN?</text>
      <rect class="field" x="1279" y="1043" width="375" height="19"/>
      <text class="question" x="1279" y="1081">THERE ARE MANY VARIATIONS OF PASSAGES?</text>
      <rect class="field" x="1279" y="1089" width="375" height="19"/>
      <path class="chevron" d="M1642,1097 L1644.5,1099.5 L1647,1097"/>
      <text class="question" x="1279" y="1127">LOREM IPSUM IS SIMPLY DUMMY TEXT OF THE PRINTING?</text>
      <rect class="field" x="1279" y="1135" width="375" height="19"/>
    </g>

    <rect class="btn-dark" x="1436" y="1162" width="62" height="19" rx="9.5"/>
    <text class="btn-label" x="1467" y="1173.5">SUBMIT</text>

    <line class="or-line" x1="1333" y1="1211" x2="1601" y2="1211"/>
    <circle class="or-badge" cx="1467" cy="1211" r="11"/>
    <text class="or-text" x="1467" y="1215">OR</text>

    <rect class="btn-blue" x="1396" y="1243" width="142" height="19" rx="9.5"/>
    <text class="btn-label" x="1467" y="1254.5">LOOK UP OUR CATALOGUE FOR PART NUMBER</text>

    <use href="#footer-wave" x="1099" y="1296" width="736" height="46"/>
    <text class="footer-text" x="1467" y="1325">© 2022 <tspan class="em">ROLLVANE SUPPLY</tspan>. All Rights Reserved.</text>
  </g>

  <!-- ========== Request a quote ========== -->
  <g class="screen request-quote">
    <rect class="screen-bg" x="77" y="1098" width="735" height="414"/>
    <polygon class="band" points="77,1098 199,1098 77,1415"/>
    <polygon class="band" points="812,1195 812,1512 693,1512"/>
    <g role="img" aria-label="Photo of a swivel caster with brake">
      <ellipse cx="144" cy="1190" rx="50" ry="46" fill="url(#caster-tone)"/>
    </g>
    <g role="img" aria-label="Photo of a heavy-duty caster with polyurethane wheel">
      <ellipse cx="744" cy="1428" rx="50" ry="52" fill="url(#caster-tone-warm)"/>
    </g>
    <use href="#brand-crest" x="364" y="1098" width="160" height="85"/>
    <text class="screen-title" x="444" y="1233">REQUEST A QUOTE</text>

    <rect class="field" x="326" y="1256" width="237" height="17"/>
    <text class="placeholder" x="333" y="1267">Manufacturer Name</text>
    <rect class="field" x="326" y="1283" width="237" height="17"/>
    <text class="placeholder" x="333" y="1294">Manufacturers Part #</text>
    <rect class="field" x="326" y="1310" width="237" height="17"/>
    <text class="placeholder" x="333" y="1321">Quantity needed</text>

    <rect class="btn-dark" x="414" y="1336" width="61" height="19" rx="9.5"/>
    <text class="btn-label" x="444.5" y="1347.5">SUBMIT</text>

    <line class="or-line" x1="311" y1="1385" x2="578" y2="1385"/>
    <circle class="or-badge" cx="444" cy="1385" r="11"/>
    <text class="or-text" x="444" y="1389">OR</text>

    <rect class="btn-blue" x="314" y="1416" width="111" height="19" rx="9.5"/>
    <text class="btn-label" x="369.5" y="1427.5">ANSWER FOR THESE QUESTIONS</text>
    <rect class="btn-dark" x="433" y="1416" width="142" height="19" rx="9.5"/>
    <text class="btn-label" x="504" y="1427.5">LOOK UP OUR CATALOGUE FOR PART NUMBER</text>

    <use href="#footer-wave" x="77" y="1466" width="735" height="46"/>
    <text class="footer-text" x="444" y="1495">© 2022 <tspan class="em">ROLLVANE SUPPLY</tspan>. All Rights Reserved.</text>
  </g>

  <!-- ========== Catalogue ========== -->
  <g class="screen catalogue">
    <rect class="screen-bg" x="1099" y="1399" width="736" height="452"/>
    <polygon class="band" points="1099,1399 1221,1399 1099,1716"/>
    <polygon class="band" points="1835,1534 1835,1851 1716,1851"/>
    <g role="img" aria-label="Photo of a swivel caster with brake">
      <ellipse cx="1168" cy="1492" rx="50" ry="46" fill="url(#caster-tone)"/>
    </g>
    <g role="img" aria-label="Photo of a heavy-duty caster with polyurethane wheel">
      <ellipse cx="1766" cy="1770" rx="50" ry="52" fill="url(#caster-tone-warm)"/>
    </g>
    <use href="#brand-crest" x="1387" y="1399" width="160" height="85"/>
    <text class="screen-title" x="1467" y="1534">OUR CATALOGUE</text>

    <g class="catalogue-grid">
      <use href="#pdf-pin" x="1248" y="1553" width="60" height="66"/>
      <text class="catalogue-label" x="1278" y="1631">CATALOGUE 01</text>
      <use href="#pdf-pin" x="1374" y="1553" width="60" height="66"/>
      <text class="catalogue-label" x="1404" y="1631">CATALOGUE 02</text>
      <use href="#pdf-pin" x="1500" y="1553" width="60" height="66"/>
      <text class="catalogue-label" x="1530" y="1631">CATALOGUE 03</text>
      <use href="#pdf-pin" x="1627" y="1553" width="60" height="66"/>
      <text class="catalogue-label" x="1657" y="1631">CATALOGUE 04</text>
      <use href="#pdf-pin" x="1248" y="1647" width="60" height="66"/>
      <text class="catalogue-label" x="1278" y="1726">CATALOGUE 05</text>
      <use href="#pdf-pin" x="1374" y="1647" width="60" height="66"/>
      <text class="catalogue-label" x="1404" y="1726">CATALOGUE 06</text>
      <use href="#pdf-pin" x="1500" y="1647" width="60" height="66"/>
      <text class="catalogue-label" x="1530" y="1726">CATALOGUE 07</text>
      <use href="#pdf-pin" x="1627" y="1647" width="60" height="66"/>
      <text class="catalogue-label" x="1657" y="1726">CATALOGUE 08</text>
    </g>

    <rect class="btn-blue" x="1436" y="1746" width="62" height="19" rx="9.5"/>
    <text class="btn-label" x="1467" y="1757.5">BACK TO FORM</text>

    <use href="#footer-wave" x="1099" y="1805" width="736" height="46"/>
    <text class="footer-text" x="1467" y="1834">© 2022 <tspan class="em">ROLLVANE SUPPLY</tspan>. All Rights Reserved.</text>
  </g>

  <!-- ========== Flow arrows ========== -->
  <g class="flow">
    <line class="flow-arrow" x1="812" y1="736" x2="1008" y2="736" marker-end="url(#arrow-head)"/>
    <line class="flow-arrow" x1="462" y1="833" x2="462" y2="1029" marker-end="url(#arrow-head)"/>
    <line class="flow-arrow" x1="665" y1="833" x2="1086" y2="1381" marker-end="url(#arrow-head)"/>
    <line class="flow-arrow" x1="733" y1="1098" x2="1082" y2="409" marker-end="url(#arrow-head)"/>
    <line class="flow-arrow" x1="812" y1="1293" x2="1070" y2="1047" marker-end="url(#arrow-head)"/>
    <line class="flow-arrow" x1="812" y1="1512" x2="959" y2="1641" marker-end="url(#arrow-head)"/>
    <line class="flow-arrow" x1="1099" y1="1463" x2="903" y2="1463" marker-end="url(#arrow-head)"/>
  </g>
</svg>
</div>
</body>
</html>
```